Brontiva - Reaching Rigor@Pace

I would like to have a 10-slides powerpoint to introduce my company Brontiva, and the concept of Continuous Verification. Continuous Verification is about how to combine Continuous Testing with ML-Driven Test Observability, in order to achieve fully automated Delivery Toolchains, supported by intelligent Quality Gates.

Target Market(s)

Swiss market, Large and medium Swiss Banks, Insurances, Pharma and Industry running large scale DevOps teams and suffer from slow/bad testing

Industry/Entity Type

IT

Font styles to use
Sans Serif

Colors
FFC000
F8CF3A
FAE287
FDF2CF
FEFAEE
F0912C
F2A743
F7CA91
FBE8D2
FDF5EE

Requirements
Must have
• Emphasizing engineering, innovation and agile/DevOps. Machine Learning and AI will lead to fully automated DevOps toolchain, including testing. We support this transformation.

```html
<!DOCTYPE html>
<html lang="en">
<head>
<meta charset="utf-8">
<title>Brontiva – Effective Continuous Verification</title>
<link rel="stylesheet" href="https://fonts.googleapis.com/css2?family=Roboto:wght@300;400;500;700&display=swap">
<style>
:root{
  --yellow:#ffc000;
  --orange:#f0912c;
  --orange-soft:#f2a743;
  --peach:#fbe8d2;
  --gold:#dba12f;
  --bronze:#a87224;
  --navy:#1f3766;
  --ink:#222;
  --text:#333;
  --muted:#666;
  --page:#dedede;
  --white:#fff;
}
*{box-sizing:border-box;margin:0;padding:0}
html,body{width:1200px;height:3966px;overflow:hidden;background:var(--page);font-family:'Roboto',sans-serif;color:var(--text)}
.deck{position:relative;width:1200px;height:3966px}
.slide{position:absolute;left:86px;width:1028px;height:578px;background:var(--white);overflow:hidden}
.header-band,.footer-band{position:absolute;left:0;width:1028px}
.header-band{top:0;height:62px}
.footer-band{bottom:0;height:46px}
.brand{position:absolute;left:60px;top:14px;display:flex;align-items:center;gap:10px}
.brand-dot{width:30px;height:30px;border-radius:50%;background:var(--orange-soft)}
.brand-name{font-size:30px;font-weight:500;color:var(--ink);letter-spacing:.5px}
.slide-title{position:absolute;right:66px;top:10px;font-size:30px;font-weight:700;color:var(--white)}
.footer-brand{position:absolute;left:218px;bottom:9px;display:flex;align-items:center;gap:6px;color:var(--white);font-size:10px;line-height:10px;letter-spacing:.5px}
.footer-brand i{display:block;width:20px;height:20px;border-radius:50%;background:var(--orange)}
.footer-brand b{font-weight:700;display:block}
.page-no{position:absolute;left:738px;bottom:17px;color:var(--white);font-size:12px;font-weight:700}

/* slide 1 */
.hero-photo{position:absolute;left:51px;top:96px;width:406px;height:406px;border-radius:50%;border:7px solid var(--orange-soft);background:radial-gradient(circle at 55% 40%,#2c8ad8,#103a78 60%,#0b2350)}
.hero-title{position:absolute;left:507px;top:152px;font-size:52px;font-weight:700;color:var(--ink);line-height:64px}
.hero-sub{position:absolute;left:507px;top:298px;font-size:32px;font-weight:300;color:#444;line-height:49px}

/* slide 2 */
.hub-card{position:absolute;width:173px;height:189px;border:2px solid;border-radius:6px;background:var(--white);text-align:center;padding:50px 8px 0}
.hub-icon{position:absolute;left:53px;top:-34px;width:64px;height:64px;border-radius:50%;border:4px solid var(--white);box-shadow:0 0 0 1px #e4e4e4}
.hub-card h3{font-size:15px;font-weight:700;color:var(--ink);line-height:20px}
.hub-card p{font-size:12px;color:var(--muted);line-height:20px;margin-top:4px}

/* slide 3 */
.purpose-card{position:absolute;left:60px;top:163px;width:906px;height:287px;border-radius:24px;background:var(--white);box-shadow:0 4px 22px rgba(0,0,0,.1);text-align:center}
.quote-mark{position:absolute;left:421px;top:42px}
.purpose-card p{position:absolute;left:60px;right:60px;top:130px;font-size:18px;line-height:39px;color:#333}

/* slide 4 */
.scope-text{position:absolute;left:57px;top:128px;width:427px}
.scope-text h2{font-size:25px;font-weight:500;line-height:36px;color:var(--ink)}
.scope-text p{font-size:19px;line-height:40px;text-align:justify;margin-top:6px}
.venn{position:absolute;left:532px;top:110px}

/* slide 5 */
.clients-title{position:absolute;left:0;width:1028px;top:102px;text-align:center;font-size:31px;font-weight:500;color:var(--ink)}
.client-tile{position:absolute;width:173px;height:96px;background:var(--white);border-radius:6px;box-shadow:0 2px 12px rgba(0,0,0,.1);display:flex;align-items:center;justify-content:center;font-size:20px;font-weight:700;color:#555}

/* slide 6 */
.offer-panel{position:absolute;top:114px;width:408px;height:363px;background:var(--white);border-radius:6px;box-shadow:0 3px 18px rgba(0,0,0,.1)}
.offer-panel h3{height:62px;background:var(--navy);color:var(--white);font-size:19px;font-weight:500;display:flex;align-items:center;justify-content:center;border-radius:6px 6px 0 0}
.offer-panel ul{list-style:none;padding:26px 26px 0 32px}
.offer-panel li{position:relative;padding-left:28px;font-size:19px;line-height:26px;color:#333;min-height:66px;display:flex;align-items:center}
.offer-panel li::before{content:"";position:absolute;left:0;top:50%;margin-top:-8px;width:16px;height:16px;border-radius:50%;border:2px solid var(--orange-soft);box-shadow:inset 0 0 0 3px var(--white),inset 0 0 0 8px var(--orange-soft)}
</style>
</head>
<body>
<div class="deck">

<!-- shared header / footer markup per slide -->
<section class="slide" style="top:86px">
  <svg class="header-band" viewBox="0 0 1028 62"><polygon points="268,0 300,0 342,62 310,62" fill="var(--yellow)"/><polygon points="300,0 1028,0 1028,62 342,62" fill="var(--orange)"/></svg>
  <div class="brand"><span class="brand-dot"></span><span class="brand-name">Brontiva</span></div>
  <div class="hero-photo" role="img" aria-label="Photo of a hand touching glowing blue gear and code icons"></div>
  <h1 class="hero-title">Effective Continuous<br>Verification</h1>
  <p class="hero-sub">Holistic Transformation with<br>the right mix &nbsp;of Expertise &amp;<br>Technologies</p>
  <svg class="footer-band" viewBox="0 0 1028 46"><polygon points="180,0 226,0 200,46 154,46" fill="var(--yellow)"/><polygon points="226,0 1028,0 1028,46 200,46" fill="var(--orange-soft)"/><rect x="0" y="41" width="1028" height="5" fill="var(--orange)"/></svg>
  <div class="footer-brand"><i></i><span><b>ALPINE</b>DIGITAL CIRCLE</span></div>
  <div class="page-no">Page.No : 01</div>
</section>

<section class="slide" style="top:730px">
  <svg class="header-band" viewBox="0 0 1028 62"><polygon points="268,0 300,0 342,62 310,62" fill="var(--yellow)"/><polygon points="300,0 1028,0 1028,62 342,62" fill="var(--orange)"/></svg>
  <div class="brand"><span class="brand-dot"></span><span class="brand-name">Brontiva</span></div>
  <h2 class="slide-title">One Hub.Multiple Expertise</h2>
  <div class="hub-card" style="left:60px;top:171px;border-color:#9cc4ee"><span class="hub-icon" style="background:#1a6fd6"></span><h3>Cloud Builders<br>Zürich</h3><p>Designing &amp; building the Digital Highway for Continuous Software Delivery</p></div>
  <div class="hub-card" style="left:243px;top:270px;border-color:#9ad3f2"><span class="hub-icon" style="background:#2ea6e6"></span><h3>Data Engineers<br>Basel</h3><p>Designing &amp; building the Digital Highway for Data- &amp; ML-driven systems</p></div>
  <div class="hub-card" style="left:427px;top:171px;border-color:#a8c3ad"><span class="hub-icon" style="background:#3f7a4f"></span><h3>Change Strategy<br>Advisors</h3><p>Culture-first, holistic transformation to establish key Capabilities of the Digital Highway</p></div>
  <div class="hub-card" style="left:610px;top:270px;border-color:#f7ca91"><span class="hub-icon" style="background:var(--orange)"></span><h3>Brontiva</h3><p>Effective Continuous Verification to enable Quality @ Speed within the Digital Highway</p></div>
  <div class="hub-card" style="left:793px;top:171px;border-color:#a9e6df"><span class="hub-icon" style="background:#4fd1c5"></span><h3>Innovation Lab<br>Partner</h3><p>Designing &amp; building effective training &amp; innovation programs to build &amp; operate the Digital Highway</p></div>
  <svg class="footer-band" viewBox="0 0 1028 46"><polygon points="180,0 226,0 200,46 154,46" fill="var(--yellow)"/><polygon points="226,0 1028,0 1028,46 200,46" fill="var(--orange-soft)"/><rect x="0" y="41" width="1028" height="5" fill="var(--orange)"/></svg>
  <div class="footer-brand"><i></i><span><b>ALPINE</b>DIGITAL CIRCLE</span></div>
  <div class="page-no">Page.No : 02</div>
</section>

<section class="slide" style="top:1374px">
  <svg class="header-band" viewBox="0 0 1028 62"><polygon points="268,0 300,0 342,62 310,62" fill="var(--yellow)"/><polygon points="300,0 1028,0 1028,62 342,62" fill="var(--orange)"/></svg>
  <div class="brand"><span class="brand-dot"></span><span class="brand-name">Brontiva</span></div>
  <h2 class="slide-title">Our Purpose</h2>
  <div class="purpose-card">
    <svg class="quote-mark" width="64" height="48" viewBox="0 0 64 48"><path d="M0 48V28C0 12 8 3 24 0l3 6C17 9 13 15 13 22h13v26H0zM36 48V28C36 12 44 3 60 0l3 6C53 9 49 15 49 22h13v26H36z" fill="var(--orange-soft)"/></svg>
    <p>We are one hub of collaborative cells, each dedicated to a niche &nbsp;capability. While enabling and facilitating people-centric innovation and &nbsp;transformation, our collective purpose is to sustainably empower &nbsp;organizations to deliver reliable digital solutions</p>
  </div>
  <svg class="footer-band" viewBox="0 0 1028 46"><polygon points="180,0 226,0 200,46 154,46" fill="var(--yellow)"/><polygon points="226,0 1028,0 1028,46 200,46" fill="var(--orange-soft)"/><rect x="0" y="41" width="1028" height="5" fill="var(--orange)"/></svg>
  <div class="footer-brand"><i></i><span><b>ALPINE</b>DIGITAL CIRCLE</span></div>
  <div class="page-no">Page.No : 03</div>
</section>

<section class="slide" style="top:2018px">
  <svg class="header-band" viewBox="0 0 1028 62"><polygon points="268,0 300,0 342,62 310,62" fill="var(--yellow)"/><polygon points="300,0 1028,0 1028,62 342,62" fill="var(--orange)"/></svg>
  <div class="brand"><span class="brand-dot"></span><span class="brand-name">Brontiva</span></div>
  <h2 class="slide-title">Definition and Scope</h2>
  <div class="scope-text">
    <h2>Effective Continuous<br>Verification (CV) is</h2>
    <p>The application of a systematic, holistic and disciplined approach for the design, implementation and cost-effective data collection, processing &amp; analytics to implement quality gates through the delivery pipelines, automate their verification and increase the overall testing &amp; SRE productivity.</p>
  </div>
  <svg class="venn" width="460" height="390" viewBox="0 0 460 390" font-family="Roboto, sans-serif" font-weight="500" text-anchor="middle">
    <circle cx="115" cy="122" r="115" fill="var(--gold)"/>
    <circle cx="337" cy="133" r="115" fill="var(--bronze)"/>
    <circle cx="213" cy="272" r="115" fill="var(--yellow)"/>
    <circle cx="209" cy="192" r="70" fill="var(--white)"/>
    <text x="102" y="82" fill="#fff" font-size="14">Quality Gates</text>
    <text x="102" y="103" fill="#fff" font-size="14">Verification Autimation</text>
    <text x="350" y="85" fill="#fff" font-size="14">Increase testing &amp;SRE</text>
    <text x="350" y="106" fill="#fff" font-size="14">Productivity for High</text>
    <text x="350" y="127" fill="#fff" font-size="14">Velocity Delivery</text>
    <text x="209" y="187" fill="#333" font-size="12" font-weight="400">THe Effective CV</text>
    <text x="209" y="206" fill="#333" font-size="12" font-weight="400">Engineering Scope</text>
    <text x="213" y="292" fill="#fff" font-size="14">Resiliency Verification</text>
    <text x="213" y="313" fill="#fff" font-size="14">Automation</text>
  </svg>
  <svg class="footer-band" viewBox="0 0 1028 46"><polygon points="180,0 226,0 200,46 154,46" fill="var(--yellow)"/><polygon points="226,0 1028,0 1028,46 200,46" fill="var(--orange-soft)"/><rect x="0" y="41" width="1028" height="5" fill="var(--orange)"/></svg>
  <div class="footer-brand"><i></i><span><b>ALPINE</b>DIGITAL CIRCLE</span></div>
  <div class="page-no">Page.No : 04</div>
</section>

<section class="slide" style="top:2662px">
  <svg class="header-band" viewBox="0 0 1028 62"><polygon points="268,0 300,0 342,62 310,62" fill="var(--yellow)"/><polygon points="300,0 1028,0 1028,62 342,62" fill="var(--orange)"/></svg>
  <div class="brand"><span class="brand-dot"></span><span class="brand-name">Brontiva</span></div>
  <h2 class="clients-title">First-class services for Swiss Leading Enterprises</h2>
  <div class="client-tile" style="left:62px;top:174px">Corvane Bank</div>
  <div class="client-tile" style="left:245px;top:174px">Altavia</div>
  <div class="client-tile" style="left:428px;top:174px">Pharmeon</div>
  <div class="client-tile" style="left:611px;top:174px">Lakeside Credit</div>
  <div class="client-tile" style="left:793px;top:174px">Rhenova</div>
  <div class="client-tile" style="left:62px;top:293px">Clinica Nordtal</div>
  <div class="client-tile" style="left:245px;top:293px;font-size:17px">Securitas Fidem</div>
  <div class="client-tile" style="left:428px;top:293px">aeroway</div>
  <div class="client-tile" style="left:611px;top:293px">Postalis Pay</div>
  <div class="client-tile" style="left:793px;top:293px;font-size:17px">Kantonal Sparbank</div>
  <div class="client-tile" style="left:62px;top:411px">enerva</div>
  <div class="client-tile" style="left:245px;top:411px;font-size:16px">Rheintal Landesbank</div>
  <div class="client-tile" style="left:428px;top:411px">Pristor</div>
  <svg class="footer-band" viewBox="0 0 1028 46"><polygon points="180,0 226,0 200,46 154,46" fill="var(--yellow)"/><polygon points="226,0 1028,0 1028,46 200,46" fill="var(--orange-soft)"/><rect x="0" y="41" width="1028" height="5" fill="var(--orange)"/></svg>
  <div class="footer-brand"><i></i><span><b>ALPINE</b>DIGITAL CIRCLE</span></div>
  <div class="page-no">Page.No : 05</div>
</section>

<section class="slide" style="top:3306px">
  <svg class="header-band" viewBox="0 0 1028 62"><polygon points="268,0 300,0 342,62 310,62" fill="var(--yellow)"/><polygon points="300,0 1028,0 1028,62 342,62" fill="var(--orange)"/></svg>
  <div class="brand"><span class="brand-dot"></span><span class="brand-name">Brontiva</span></div>
  <h2 class="slide-title">Our Offering Portfolio</h2>
  <div class="offer-panel" style="left:65px">
    <h3>One Partner for Your Effective CV Journey</h3>
    <ul>
      <li>Maturity Assessment, Target Definition &amp; Transformation Roadmap</li>
      <li>Effective CV Architecture &amp; Tooling</li>
      <li>Effective CV Training &amp; Coaching</li>
      <li>Effective CV Engineering Services</li>
    </ul>
  </div>
  <div class="offer-panel" style="left:554px">
    <h3>One Partner for Multiple C V Practices</h3>
    <ul>
      <li>Continuous Performance Verification</li>
      <li>Continuous Security Verification</li>
      <li>Continuous Functional Verification</li>
      <li>Chaos engineering</li>
    </ul>
  </div>
  <svg class="footer-band" viewBox="0 0 1028 46"><polygon points="180,0 226,0 200,46 154,46" fill="var(--yellow)"/><polygon points="226,0 1028,0 1028,46 200,46" fill="var(--orange-soft)"/><rect x="0" y="41" width="1028" height="5" fill="var(--orange)"/></svg>
  <div class="footer-brand"><i></i><span><b>ALPINE</b>DIGITAL CIRCLE</span></div>
  <div class="page-no">Page.No : 06</div>
</section>

</div>
</body>
</html>
```